Redone of Site on Wix

Project Overview: Website Redesign for Brovanta
We are looking to redesign our current website, www.brovantausa.com, to better match the style and functionality of these reference sites:
Quorin Health
MZT FlexBit
Key Requirements: Modern, Clean Design:
The site should have a professional and clean layout with clear messaging about our services.
Visual Elements: Use strong visuals like images, icons, or illustrations to support text and engage visitors.
Clear Service Breakdown: Easily digestible sections explaining what Brovanta offers, similar to the service explanations on the reference sites.
User-Friendly Navigation: Simple, intuitive navigation with visible CTAs (e.g., "Learn More," "Get Started").
Trust-Building Features: Incorporate trust elements like client logos, testimonials, or success stories to build credibility.
Mobile-Responsive:
Ensure the website is fully responsive and looks great on all devices (desktop, tablet, mobile).
SEO Optimization:
Deliverables: Fully functional website with modern design.
All content will be provided, but we may need help with imagery or layout recommendations.
Responsive design and mobile optimization.
We are looking for a clean, modern, and easy-to-navigate site that reflects the professionalism of our brand.

```html
<!DOCTYPE html>
<html lang="en">
<head>
<meta charset="utf-8">
<title>Brovanta – Dietary Management for Sickle Cell Disease</title>
<link href="https://fonts.googleapis.com/css2?family=Poppins:ital,wght@0,400;0,500;0,600;0,700;1,400;1,600&display=swap" rel="stylesheet">
<style>
:root{
  --red:#c4262e;
  --red-dark:#b3252b;
  --ink:#1d1d1f;
  --muted:#555;
  --pink:#fdeeee;
  --pink-soft:#fdf3f3;
  --line:#d9d9d9;
  --white:#fff;
}
*{box-sizing:border-box;margin:0;padding:0}
html,body{width:1200px;height:4681px;overflow:hidden}
body{font-family:'Poppins',sans-serif;color:var(--ink);background:var(--white);position:relative}
.abs{position:absolute}
.red{color:var(--red)}
.btn{position:absolute;display:flex;align-items:center;justify-content:center;gap:8px;font-size:16px;border-radius:2px;text-decoration:none}
.btn-solid{background:var(--red);color:#fff}
.btn-outline{border:1.5px solid var(--red);color:var(--red);background:#fff}
.chev{width:8px;height:12px}

/* header */
.site-header{position:absolute;top:0;left:0;width:1200px;height:113px;background:#fff;border-bottom:1px solid #eee}
.brand{position:absolute;left:60px;top:24px;font-size:48px;font-weight:500;color:var(--red);letter-spacing:1px}
.menu{position:absolute;left:1072px;top:40px;width:60px}
.menu span{display:block;height:3px;background:#222;margin-bottom:12px}

/* hero */
.hero{position:absolute;top:113px;left:0;width:1200px;height:562px;background:var(--pink)}
.hero-photo{position:absolute;right:0;top:0;width:740px;height:562px;clip-path:polygon(22% 0,100% 0,100% 100%,0 100%);
  background:linear-gradient(120deg,#e9dccd 0%,#c9a27c 35%,#7a5236 60%,#3d2a20 80%,#b99a7c 100%)}
.hero h1{position:absolute;left:60px;top:70px;font-size:46px;line-height:54px;font-weight:600}
.hero p{position:absolute;left:60px;top:205px;width:480px;font-size:18px;line-height:30px;color:#444}

/* trusted */
.trusted-label{position:absolute;left:60px;top:700px;font-size:18px;font-weight:600}
.logos{position:absolute;left:60px;top:744px;width:1085px;display:flex;justify-content:space-between;align-items:center}
.logo-item{display:flex;align-items:center;gap:8px;font-size:22px;font-weight:600;color:#444}
.logo-item i{display:block;width:22px;height:22px;background:#444;border-radius:4px}

/* section headings */
.sec-title{position:absolute;left:0;width:1200px;text-align:center;font-size:38px;font-weight:600}

/* benefits */
.card{position:absolute;background:#fff;border-radius:6px;box-shadow:0 4px 14px rgba(0,0,0,.12)}
.benefit{top:980px;width:342px;height:244px;text-align:center}
.benefit svg{margin-top:24px}
.benefit h3{font-size:22px;font-weight:600;margin-top:10px}
.benefit p{font-size:16px;line-height:27px;color:#555;margin:12px 24px 0}

/* understanding */
.band-pink{position:absolute;left:0;width:1200px;background:var(--pink)}
.scd-visual{position:absolute;left:60px;top:1375px;width:549px;height:397px;border-radius:6px;
  background:radial-gradient(circle at 55% 65%,#e0343b 0%,#a8141d 35%,#5b0b12 70%,#2b0508 100%);color:#fff}
.scd-visual .k1{position:absolute;left:38px;top:8px;font-size:28px;font-weight:400}
.scd-visual .k2{position:absolute;left:44px;top:34px;font-size:96px;font-weight:600;line-height:110px}
.scd-visual .k3{position:absolute;left:50px;top:130px;font-size:15px;letter-spacing:3px;font-weight:500}
.block h2{font-size:38px;font-weight:600;line-height:46px}
.block p{font-size:18px;line-height:30px;color:#333;margin-top:20px}
.link{display:flex;align-items:center;gap:10px;color:var(--red);font-size:16px;margin-top:30px}
.hcp-visual{position:absolute;left:615px;top:1815px;width:528px;height:400px;border-radius:48% 40% 10% 40%;
  background:linear-gradient(135deg,#b8bcf5 0%,#8f95ea 45%,#3a8fd8 75%,#e6a5a8 100%)}

/* support */
.support{top:2470px;width:525px;height:245px}
.support svg{position:absolute;left:30px;top:28px}
.support h3{position:absolute;left:30px;top:118px;font-size:22px;font-weight:600}
.support p{position:absolute;left:30px;top:162px;width:440px;font-size:16px;line-height:27px;color:#555}

/* heroes */
.quote{top:2970px;width:525px;height:242px;text-align:center;padding:0 24px;overflow:hidden}
.quote .mark{position:absolute;left:50%;top:40px;transform:translateX(-50%);font-size:160px;line-height:120px;color:#f3c3c5;font-weight:700;font-family:Georgia,serif}
.quote p{position:relative;margin-top:74px;font-size:17px;line-height:27px;font-style:italic}
.quote .who{position:relative;margin-top:28px;font-size:22px}
.fade{opacity:.4}

/* resources */
.res-item{position:absolute;left:573px;width:567px;height:175px;border-bottom:1.5px solid var(--line)}
.res-item h4{position:absolute;left:0;top:78px;font-size:22px;font-weight:600}
.res-item a{position:absolute;left:0;top:122px;font-size:16px;color:var(--red);display:flex;align-items:center;gap:6px}

/* footer */
.site-footer{position:absolute;left:0;top:4335px;width:1200px;height:346px;background:var(--red-dark);color:#fff}
.site-footer h5{position:absolute;top:70px;font-size:22px;font-weight:600}
.site-footer ul{position:absolute;top:125px;list-style:none;font-size:15px;line-height:25px}
.foot-rule{position:absolute;left:60px;top:265px;width:1080px;height:1px;background:rgba(255,255,255,.45)}
</style>
</head>
<body>

<header class="site-header">
  <div class="brand">Brovanta</div>
  <a class="btn btn-outline" style="left:836px;top:35px;width:211px;height:42px;font-size:16px">Request Information</a>
  <div class="menu"><span></span><span></span><span></span></div>
</header>

<section class="hero">
  <div class="hero-photo" role="img" aria-label="Photo of a mother and young children preparing food together in a sunny kitchen"></div>
  <h1>Dietary Management<br>For Sickle Cell <span class="red">Disease</span></h1>
  <p><i>BROVANTA</i> is a medical food product designed for the dietary management of Sickle Cell Disease in both pediatric and adult patients.</p>
  <a class="btn btn-solid" style="left:60px;top:340px;width:216px;height:40px">Request a Sample <svg class="chev" viewBox="0 0 8 12"><path d="M1 1l5 5-5 5" stroke="#fff" stroke-width="1.8" fill="none"/></svg></a>
  <a class="btn btn-outline" style="left:291px;top:340px;width:127px;height:40px">Learn More</a>
</section>

<div class="trusted-label">Trusted By:</div>
<div class="logos">
  <div class="logo-item"><i></i>Mervale</div>
  <div class="logo-item">Ostrin</div>
  <div class="logo-item"><i></i>Palvique</div>
  <div class="logo-item"><i></i>Tendra</div>
  <div class="logo-item"><i></i>Quillbay</div>
</div>

<h2 class="sec-title" style="top:870px">Key <span class="red">Benefits</span> of BRO<i>VANTA</i></h2>

<div class="card benefit" style="left:60px">
  <svg width="70" height="76" viewBox="0 0 70 76" fill="none" stroke="#c4262e" stroke-width="2"><rect x="8" y="6" width="40" height="52" rx="2"/><path d="M16 18h24M16 26h24M16 34h14"/><circle cx="44" cy="50" r="12"/><path d="M52 59l12 12"/></svg>
  <h3>Scientifically Formulated</h3>
  <p>Specifically designed for dietary management of Sickle Cell Disease</p>
</div>
<div class="card benefit" style="left:429px">
  <svg width="70" height="76" viewBox="0 0 70 76" fill="none" stroke="#c4262e" stroke-width="2"><rect x="12" y="6" width="46" height="62" rx="3"/><circle cx="35" cy="34" r="10"/><path d="M20 56h30M20 62h20"/></svg>
  <h3>Easy Administration</h3>
  <p>Simple dosing schedule that fits into your daily routine</p>
</div>
<div class="card benefit" style="left:798px">
  <svg width="76" height="76" viewBox="0 0 76 76" fill="none" stroke="#c4262e" stroke-width="2"><circle cx="38" cy="22" r="10"/><path d="M6 60l14-18 10 12M70 60L56 42 46 54M20 68h36"/></svg>
  <h3>Comprehensive Support</h3>
  <p>Access to patient support services and resources</p>
</div>

<div class="band-pink" style="top:1300px;height:992px"></div>
<div class="scd-visual" role="img" aria-label="Illustration of a sickle-shaped red blood cell on a dark red background">
  <div class="k1">Understanding</div>
  <div class="k2">SCD</div>
  <div class="k3">SICKLE CELL DISEASE</div>
</div>
<div class="abs block" style="left:718px;top:1448px;width:430px">
  <h2>Understanding <span class="red">SCD</span></h2>
  <p>Sickle Cell Disease affects millions worldwide. Learn about the medical challenges and how BROVANTA can help in dietary management.</p>
  <div class="link">Learn More About SCD <svg class="chev" viewBox="0 0 8 12"><path d="M1 1l5 5-5 5" stroke="#c4262e" stroke-width="1.8" fill="none"/></svg></div>
</div>
<div class="abs block" style="left:64px;top:1870px;width:420px">
  <h2>For <span class="red">Healthcare</span><br>Professionals</h2>
  <p>Access prescribing information and clinical resources to help manage your patients with Sickle Cell Disease.</p>
  <div class="link" style="margin-top:50px">View Professional Resources <svg class="chev" viewBox="0 0 8 12"><path d="M1 1l5 5-5 5" stroke="#c4262e" stroke-width="1.8" fill="none"/></svg></div>
</div>
<div class="hcp-visual" role="img" aria-label="Illustration of three healthcare professionals in scrubs holding clipboards"></div>

<h2 class="sec-title" style="top:2360px">Patient Support <span class="red">Services</span></h2>
<div class="card support" style="left:60px">
  <svg width="70" height="70" viewBox="0 0 24 24" fill="#e15a60"><path d="M6.6 10.8a15.1 15.1 0 006.6 6.6l2.2-2.2a1 1 0 011-.25 11.4 11.4 0 003.6.57 1 1 0 011 1V20a1 1 0 01-1 1A17 17 0 013 4a1 1 0 011-1h3.5a1 1 0 011 1c0 1.25.2 2.45.57 3.57a1 1 0 01-.25 1z"/></svg>
  <h3>24/7 Support</h3>
  <p>Specifically designed for dietary management of Sickle Cell Disease</p>
</div>
<div class="card support" style="left:615px">
  <svg width="74" height="70" viewBox="0 0 74 70" fill="none" stroke="#c4262e" stroke-width="2.2"><rect x="4" y="6" width="40" height="40" rx="3"/><text x="10" y="34" font-size="18" fill="#c4262e" stroke="none" font-family="Poppins,sans-serif">24</text><path d="M44 22h14l12 14v16H44z"/><circle cx="16" cy="56" r="6"/><circle cx="56" cy="56" r="6"/></svg>
  <h3>Shipping Support</h3>
  <p>Specifically designed for dietary management of Sickle Cell Disease</p>
</div>

<div class="band-pink" style="top:2790px;height:520px;background:var(--pink-soft)"></div>
<h2 class="sec-title" style="top:2862px">BRO<i>VANTA</i> <span class="red">HEROES</span></h2>
<div class="card quote fade" style="left:-218px">
  <div class="mark">"</div>
  <p>"Lorem ipsum dolor sit amet, consectetur adipiscing elit. Sed do eiusmod tempor incididunt ut labore et dolore magna aliqua."</p>
  <div class="who">- Patient Name</div>
</div>
<div class="card quote" style="left:337px">
  <div class="mark">"</div>
  <p>"Lorem ipsum dolor sit amet, consectetur adipiscing elit. Sed do eiusmod tempor incididunt ut labore et dolore magna aliqua."</p>
  <div class="who">- Patient Name</div>
</div>
<div class="card quote fade" style="left:892px">
  <div class="mark">"</div>
  <p>"Lorem ipsum dolor sit amet, consectetur adipiscing elit. Sed do eiusmod tempor incididunt ut labore et dolore magna aliqua."</p>
  <div class="who">- Patient Name</div>
</div>

<div class="abs block" style="left:60px;top:3385px"><h2>Explore our<br>Helpful <span class="red">Resources</span></h2></div>
<div class="res-item" style="top:3370px">
  <svg class="abs" style="left:0;top:20px" width="50" height="50" viewBox="0 0 50 50" fill="none" stroke="#c4262e" stroke-width="2.5"><path d="M25 4v28M14 22l11 11 11-11M4 36v10h42V36"/></svg>
  <h4>Patient Information Sheet</h4><a>Download PDF <svg class="chev" viewBox="0 0 8 12"><path d="M1 1l5 5-5 5" stroke="#c4262e" stroke-width="1.8" fill="none"/></svg></a>
</div>
<div class="res-item" style="top:3545px">
  <svg class="abs" style="left:0;top:20px" width="50" height="50" viewBox="0 0 50 50" fill="none" stroke="#c4262e" stroke-width="2.5"><path d="M25 4v28M14 22l11 11 11-11M4 36v10h42V36"/></svg>
  <h4>Dosing Guidelines</h4><a>Download PDF <svg class="chev" viewBox="0 0 8 12"><path d="M1 1l5 5-5 5" stroke="#c4262e" stroke-width="1.8" fill="none"/></svg></a>
</div>
<div class="res-item" style="top:3720px">
  <svg class="abs" style="left:0;top:20px" width="50" height="50" viewBox="0 0 50 50" fill="none" stroke="#c4262e" stroke-width="2.5"><path d="M25 4v28M14 22l11 11 11-11M4 36v10h42V36"/></svg>
  <h4>Frequently Asked Questions</h4><a>Download PDF <svg class="chev" viewBox="0 0 8 12"><path d="M1 1l5 5-5 5" stroke="#c4262e" stroke-width="1.8" fill="none"/></svg></a>
</div>

<div class="band-pink" style="top:3970px;height:365px;background:var(--pink-soft)"></div>
<h2 class="sec-title" style="top:4060px">Ready to Learn More <span class="red">About BRO<i>VANTA</i></span>?</h2>
<p class="abs" style="left:0;top:4135px;width:1200px;text-align:center;font-size:17px">Connect with our team to get started</p>
<a class="btn btn-solid" style="left:420px;top:4187px;width:214px;height:40px">Request a Sample <svg class="chev" viewBox="0 0 8 12"><path d="M1 1l5 5-5 5" stroke="#fff" stroke-width="1.8" fill="none"/></svg></a>
<a class="btn btn-outline" style="left:651px;top:4187px;width:128px;height:40px">Contact Us</a>

<footer class="site-footer">
  <div class="abs" style="left:60px;top:42px;font-size:48px;font-weight:500">Brovanta</div>
  <p class="abs" style="left:60px;top:148px;width:340px;font-size:17px;line-height:28px">A medical food for the dietary management of Sickle Cell Disease</p>
  <h5 style="left:456px">Quick Links</h5>
  <ul style="left:456px"><li>About BROVANTA</li><li>About SCD</li><li>Healthcare Professionals</li></ul>
  <h5 style="left:692px">Support</h5>
  <ul style="left:692px"><li>Patient Support</li><li>Contact Us</li><li>FAQ</li></ul>
  <h5 style="left:897px">Connect With Us</h5>
  <ul style="left:897px;line-height:40px">
    <li style="display:flex;align-items:center;gap:12px"><svg width="18" height="18" viewBox="0 0 24 24" fill="#fff"><path d="M6.6 10.8a15.1 15.1 0 006.6 6.6l2.2-2.2a1 1 0 011-.25 11.4 11.4 0 003.6.57 1 1 0 011 1V20a1 1 0 01-1 1A17 17 0 013 4a1 1 0 011-1h3.5a1 1 0 011 1c0 1.25.2 2.45.57 3.57a1 1 0 01-.25 1z"/></svg>1-800-XXX-XXXX</li>
    <li style="display:flex;align-items:center;gap:12px"><svg width="20" height="15" viewBox="0 0 20 15" fill="none" stroke="#fff" stroke-width="1.5"><rect x="1" y="1" width="18" height="13"/><path d="M1 1l9 7 9-7"/></svg>support@brovantausa.com</li>
  </ul>
  <div class="foot-rule"></div>
  <p class="abs" style="left:0;top:290px;width:1200px;text-align:center;font-size:14px">© 2025 BROVANTA. All rights reserved.</p>
</footer>

</body>
</html>
```